use my brand and make an elegant business card  with it

Target Market(s)
male and female ' ages 25 to 45 age- who appreciate the highest quality goods, experiences, services, brands and relationships
Industry/Entity Type
Business
Requirements
Must have
- my logo integrated into the design-note the uploaded file
front: just logo and the phrase: New. Trend. Life. Style
back informations:
Mirela Dostan
Director
phone: +1 604 5290417
www.midostan.com
email: mireladostan@midostan.com
the pin of Facebook (F) and tweeter (T)
Nice to have
- contrast of the colors black gold and silver
Should not have
- cartoons or whimsical design

```html
<!DOCTYPE html>
<html lang="en">
<head>
<meta charset="utf-8">
<title>Mi Dostan — Business Card</title>
<link href="https://fonts.googleapis.com/css2?family=Montserrat:wght@300;400;500&display=swap" rel="stylesheet">
<style>
  :root {
    --stage: #2b2b2b;
    --card-black: #0d0d0d;
    --card-white: #fbfbfb;
    --gold: #b8930a;
    --gold-deep: #8a6d00;
    --silver: #8f8f8f;
    --ink-grey: #6f6f6f;
  }
  * { box-sizing: border-box; margin: 0; padding: 0; }
  html, body {
    width: 1200px; height: 900px; overflow: hidden;
    background: var(--stage);
    font-family: "Montserrat", Arial, sans-serif;
  }
  .stage {
    width: 1200px; height: 900px;
    display: flex; flex-direction: column; align-items: center; justify-content: center;
    gap: 36px;
  }
  .card {
    position: relative;
    width: 700px; height: 400px;
    box-shadow: 0 10px 30px rgba(0,0,0,.5);
    overflow: hidden;
  }

  /* Front */
  .card--front { background: var(--card-black); }
  .front-brand {
    position: absolute; left: 150px; top: 150px;
    display: flex; align-items: center; gap: 18px;
  }
  .brand-mark {
    width: 22px; height: 22px; border-radius: 50%;
    background: var(--gold);
  }
  .brand-name {
    font-weight: 500; font-size: 54px; letter-spacing: 6px;
    color: var(--gold); text-transform: uppercase; line-height: 1;
  }
  .front-tagline {
    position: absolute; left: 190px; top: 232px;
    font-weight: 300; font-size: 17px; letter-spacing: 5px;
    color: var(--silver); text-transform: uppercase;
  }

  /* Back */
  .card--back { background: var(--card-white); }
  .back-brand {
    position: absolute; left: 40px; top: 48px;
    display: flex; align-items: center; gap: 14px;
  }
  .back-brand .brand-name { font-size: 46px; letter-spacing: 5px; }
  .person {
    position: absolute; left: 64px; top: 196px;
  }
  .person-name { font-size: 22px; font-weight: 400; color: var(--gold); }
  .person-role { font-size: 16px; font-weight: 400; color: var(--ink-grey); margin-top: 4px; }
  .contact-list {
    list-style: none;
    font-size: 18px; font-weight: 400; color: var(--ink-grey);
  }
  .contact-list li { display: flex; align-items: center; gap: 10px; margin-bottom: 6px; }
  .contact-list svg { flex: none; }
  .contact--direct { position: absolute; left: 64px; top: 282px; }
  .contact--social { position: absolute; left: 450px; top: 196px; font-size: 17px; }
  .social-square { width: 14px; height: 14px; background: var(--gold-deep); flex: none; }
  .gold-band {
    position: absolute; left: 0; right: 0; bottom: 0; height: 34px;
    background: linear-gradient(90deg, var(--gold-deep), var(--gold));
  }
</style>
</head>
<body>
<main class="stage">
  <section class="card card--front" aria-label="Card front">
    <div class="front-brand">
      <span class="brand-mark"></span>
      <span class="brand-name">Mi Dostan</span>
    </div>
    <p class="front-tagline">New. Trend. Life. Style</p>
  </section>

  <section class="card card--back" aria-label="Card back">
    <div class="back-brand">
      <span class="brand-mark"></span>
      <span class="brand-name">Mi Dostan</span>
    </div>

    <div class="person">
      <p class="person-name">Mirela Dostan</p>
      <p class="person-role">Director</p>
    </div>

    <ul class="contact-list contact--direct">
      <li>
        <svg width="16" height="16" viewBox="0 0 16 16" aria-hidden="true">
          <circle cx="8" cy="8" r="7" fill="none" stroke="#b8930a" stroke-width="1.4"/>
          <path d="M5.5 4.5c-.6 2.8 1.8 6.4 5 7l.8-1.6-1.6-1-.8.8c-1-.5-1.8-1.4-2.2-2.4l.8-.8-1-1.6z" fill="#b8930a"/>
        </svg>
        +1 604 5290417
      </li>
      <li>
        <svg width="16" height="12" viewBox="0 0 16 12" aria-hidden="true">
          <rect x="0" y="0" width="16" height="12" fill="#b8930a"/>
          <path d="M0 0l8 6.5L16 0" fill="none" stroke="#fbfbfb" stroke-width="1.2"/>
        </svg>
        mireladostan@midostan.com
      </li>
    </ul>

    <ul class="contact-list contact--social">
      <li><span class="social-square"></span>midostan</li>
      <li><span class="social-square"></span>@midostan</li>
      <li>
        <svg width="14" height="14" viewBox="0 0 14 14" aria-hidden="true">
          <g fill="none" stroke="#8a6d00" stroke-width="1.2">
            <circle cx="7" cy="7" r="6"/>
            <ellipse cx="7" cy="7" rx="2.6" ry="6"/>
            <path d="M1 7h12"/>
          </g>
        </svg>
        www.midostan.com
      </li>
    </ul>

    <div class="gold-band"></div>
  </section>
</main>
</body>
</html>
```